Webdesign für Energieberatung
Hallo,
es geht um die Erstellung einer Website für einen Diplom Bauingenieur (FH) mit dem Schwerpunkt 'Energieberatung'.
---mit fundierten bauphysikalischen u. technischen Kenntnissen und qualifizierter Ausbildung---
Zu der Thematik - Energieberatung gehören folgende Leistungen.
1. Energetische Beratung und die Erstellung von Energiekonzepten für Bauherren aus dem privaten, gewerblichen und kommunalen Bereichen.
2. Erstellung von energieeffizienten Sanierungsstrategien für Bauherren, die Sanierungsmaßnahmen planen um die energetischen Bilanz ihrer Gebäude zu verbessern mit dem Ziel hier die optimale Lösung erreichen.
3. Bauphysikalische Spezialberechnungen wie z.B. Wärmebrücken-Berechnungen zur Optimierung der EnEV Nachweise oder zur Feststellung von Feuchteproblematiken u. der Durchführung einer Schimmelanalyse.
4. Beratung zu den angebotenen Förderprogrammen zur Energieeinsparung und der Beantragung von öffentlichen Fördermitteln von der ZPT, der DUNO und weitere - wie z.B. regionale Förderer oder Kommunen.
5. Baubegleitung zur Sicherstellung der korrekten Durchführung der festgelegten und berechneten energetischen Werte auf der Baustelle selbst mit abschliessender Qualitätskontrolle und Dokumentation.
6. Ausstellen von Energieausweisen u. die Erstellung von Energiebilanzen für Gewerbe- u. Industriegebäuden (nicht Wohngebäuden) und auch Wohnungen laut den Richtlinien der Energieeinsparverordnung - kurz EnEV und anderen europäischen Richtlinien.
7. Durchführung von bauphysikalischen Messungen wie z.B die Differenzdruckmesssungen- auch Blower-Door Messungen genannt oder die Erstellung von thermografischen Aufnahmen um Schwachstellen z.B. an der Gebäudehülle sichtbar zu machen.
8. Vor - Ort - Betreuung auf der Baustelle in enger Zusammenarbeit mit dem Bauherren, dem Architekten, dem ausführendem Bauunternehmen und weiteren Dienstleistern.
Hier wü..
Aufgabenstellung
Es gibt noch kein Logo...., würden wir aber auch gern haben wollen. Grundsätzlich sind wir offen für alles. Gerne aber im modernen Stil - große Bilder (vielleicht auf Fullscreen) oder auch Videos in Endlosschleife - markante Texte mit schöner Grafik - nicht klein gedacht, sonder ehr sehr selbstbewusst. Auffällig u. neu gedacht - mit dem gewissen i-tüpfelchen. Die Farbe 'orange' darf allerdings nicht vorkommen. Für alles andere sind wir offen. Zu der Bildfrage hatte ich ja bereits oben was geschrieben - würden wir nachliefern. Für geeignete Vorschläge wären wir dankbar.

```html
<!DOCTYPE html>
<html lang="de">
<head>
<meta charset="utf-8">
<title>Energieberatung – Leistungen</title>
<link href="https://fonts.googleapis.com/css2?family=Bebas+Neue&family=Open+Sans:wght@400;600;700&display=swap" rel="stylesheet">
<style>
  :root {
    --stage: #f7f7f7;
    --navy-deep: #15243a;
    --navy-mid: #2c3f57;
    --sky-teal: #86cbd6;
    --sky-green: #b9ddb4;
    --sky-white: #eef0f3;
    --green-dark: #0f5877;
    --green-mid: #2f8c52;
    --green-light: #6cba4c;
    --ink: #2b2b2b;
    --white: #ffffff;
    --accent-blue: #2ba3e0;
    --footer-dark: #161616;
    --head: "Bebas Neue", "Arial Narrow", sans-serif;
    --body: "Open Sans", Arial, sans-serif;
  }
  * { box-sizing: border-box; margin: 0; padding: 0; }
  html, body { width: 960px; height: 1200px; overflow: hidden; background: var(--stage); }
  body { font-family: var(--body); hyphens: auto; -webkit-hyphens: auto; }

  .page {
    position: absolute; left: 80px; top: 0; width: 800px; height: 1200px;
    box-shadow: 0 10px 24px rgba(0,0,0,.18);
    overflow: hidden;
  }
  .band { position: absolute; left: 0; width: 800px; }
  .band-media { position: absolute; inset: 0; }

  /* Header */
  .hero { top: 0; height: 189px; }
  .hero .band-media { background: linear-gradient(160deg, var(--navy-deep) 0%, var(--navy-mid) 60%, #3b4a58 100%); }
  .brand {
    position: absolute; left: 142px; top: 38px;
    display: flex; align-items: center; gap: 7px;
    font-family: var(--head); font-size: 25px; color: var(--white); letter-spacing: .5px;
  }
  .brand-square { width: 20px; height: 20px; border: 2px solid var(--white); }
  .main-nav { position: absolute; top: 41px; left: 0; width: 800px; }
  .main-nav a {
    position: absolute; font-size: 8.5px; font-weight: 700; color: var(--white); text-decoration: none;
  }
  .main-nav a.is-active { color: var(--accent-blue); }
  .eyebrow {
    position: absolute; display: flex; align-items: center; gap: 7px;
    font-family: var(--head); font-size: 11px; letter-spacing: .3px;
  }
  .eyebrow::before { content: ""; display: block; width: 35px; height: 1.5px; background: currentColor; }
  .hero .eyebrow { left: 142px; top: 107px; color: var(--white); }
  .hero-title {
    position: absolute; left: 141px; top: 127px;
    font-family: var(--head); font-size: 53px; line-height: 1; color: var(--white); letter-spacing: .5px; font-weight: 400;
  }

  /* Angebot */
  .offer { top: 189px; height: 356px; color: var(--ink); }
  .offer .band-media {
    background:
      linear-gradient(180deg, rgba(255,255,255,0) 55%, rgba(200,215,205,.35) 100%),
      linear-gradient(90deg, var(--sky-teal) 0%, var(--sky-green) 35%, #dfe9de 60%, var(--sky-white) 100%);
  }
  .section-no {
    position: absolute; left: 139px; top: 50px; font-family: var(--head); font-size: 10px; color: var(--white);
    padding-bottom: 2px; border-bottom: 1px solid var(--white); width: 39px;
  }
  .section-title {
    position: absolute; left: 137px; top: 71px;
    font-family: var(--head); font-size: 50px; line-height: 1; font-weight: 400; color: #2f2f2f; letter-spacing: .5px;
  }
  .offer .eyebrow { left: 139px; top: 120px; color: var(--ink); }
  .offer .eyebrow::before { background: var(--white); }
  .lead { position: absolute; left: 139px; top: 157px; width: 220px; font-size: 7.8px; line-height: 10.5px; }
  .columns { position: absolute; left: 139px; top: 202px; display: flex; gap: 18px; }
  .columns p { width: 110px; font-size: 7.8px; line-height: 10.5px; }

  /* Services */
  .services { top: 545px; height: 492px; color: var(--white); }
  .services .band-media {
    background:
      linear-gradient(180deg, rgba(10,60,100,.35) 0%, rgba(0,0,0,0) 40%),
      linear-gradient(100deg, var(--green-dark) 0%, var(--green-mid) 45%, var(--green-light) 100%);
  }
  .service { position: absolute; width: 128px; }
  .service-icon { display: block; width: 32px; height: 34px; }
  .service-title {
    margin-top: 18px; font-family: var(--head); font-size: 13.5px; line-height: 12.5px; font-weight: 400; letter-spacing: .3px;
  }
  .service-text { font-size: 7.4px; line-height: 10px; font-weight: 600; overflow-wrap: break-word; }
  .service-rule { position: absolute; height: 1px; width: 120px; background: rgba(255,255,255,.7); }

  /* Kontakt */
  .contact { top: 1037px; height: 163px; color: var(--white); }
  .contact .band-media { background: linear-gradient(90deg, #2a2d2a 0%, var(--footer-dark) 60%, #0e0e0e 100%); }
  .contact-title { position: absolute; left: 137px; top: 38px; font-family: var(--head); font-size: 30px; font-weight: 400; line-height: 1; letter-spacing: .5px; }
  .contact-rule { position: absolute; left: 137px; top: 72px; width: 36px; height: 1.5px; background: var(--white); }
  .contact-details { position: absolute; left: 137px; top: 86px; font-style: normal; font-size: 8px; line-height: 10.5px; font-weight: 700; }
</style>
</head>
<body>
<div class="page">

  <header class="band hero">
    <div class="band-media" role="img" aria-label="Foto: Abendhimmel mit Windrad"></div>
    <div class="brand"><span class="brand-square"></span>Energieberatung</div>
    <nav class="main-nav">
      <a href="#" style="left:477px">Über uns</a>
      <a href="#" class="is-active" style="left:526px">Leistungen</a>
      <a href="#" style="left:584px">Preise</a>
      <a href="#" style="left:623px">Kontakt</a>
    </nav>
    <div class="eyebrow">Blindtext</div>
    <h1 class="hero-title">Leistungen</h1>
  </header>

  <section class="band offer">
    <div class="band-media" role="img" aria-label="Foto: moderne Wohnanlage mit Balkonen im Gegenlicht"></div>
    <div class="section-no">02</div>
    <h2 class="section-title">Unser Angebot</h2>
    <div class="eyebrow">Blindtext</div>
    <p class="lead">Weit hinten, hinter den Wortbergen, fern der Länder Vokalien und Konsonantien leben die Blindtexte. Abgeschieden wohnen sie in Buchstabhausen.</p>
    <div class="columns">
      <p>Weit hinten, hinter den Wortbergen, fern der Länder Vokalien und Konsonantien leben die Blindtexte. Abgeschieden wohnen sie in Buchstabhausen an der Küste des Semantik, eines großen Sprachozeans. Ein kleines Bächlein namens Duden fließt durch ihren Ort und versorgt sie mit den nötigen Regelialien. Es ist ein paradiesmatisches</p>
      <p>Land, in dem einem gebratene Satzteile in den Mund fliegen. Nicht einmal von der allmächtigen Interpunktion werden die Blindtexte beherrscht – ein geradezu unorthographisches Leben. Eines Tages aber beschloß eine kleine Zeile Blindtext, ihr Name war Lorem Ipsum, hinaus zu gehen in die weite Grammatik.</p>
    </div>
  </section>

  <section class="band services">
    <div class="band-media" role="img" aria-label="Foto: begrünter Innenhof einer Wohnanlage, grün eingefärbt"></div>

    <article class="service" style="left:137px;top:36px">
      <svg class="service-icon" viewBox="0 0 32 34" fill="none" stroke="#fff" stroke-width="1.6" stroke-linecap="round" stroke-linejoin="round">
        <path d="M10 22c-3-2.5-5-5.5-5-9.5a11 11 0 0 1 22 0c0 4-2 7-5 9.5v3H10z"/><path d="M11 28h10M12.5 31h7M16 25V13M16 17l-3-3M16 15l3-3"/>
      </svg>
      <h3 class="service-title">Energetische<br>Beratung</h3>
      <p class="service-text">Weit hinten, hinter den Wortbergen, fern der Länder Vokalien und Konsonantien leben die Blindtexte. Abgeschieden wohnen sie in Buchstabhausen.</p>
    </article>
    <article class="service" style="left:277px;top:36px">
      <svg class="service-icon" viewBox="0 0 32 34" fill="none" stroke="#fff" stroke-width="1.6" stroke-linejoin="round">
        <path d="M16 2c-2 3-3 4.5-3 6a3 3 0 0 0 6 0c0-1.5-1-3-3-6zM7 11c-2 3-3 4.5-3 6a3 3 0 0 0 6 0c0-1.5-1-3-3-6zM25 11c-2 3-3 4.5-3 6a3 3 0 0 0 6 0c0-1.5-1-3-3-6zM16 18c-3 4-4.5 6-4.5 8.5a4.5 4.5 0 0 0 9 0c0-2.5-1.5-4.5-4.5-8.5z"/>
      </svg>
      <h3 class="service-title">Sanierungs-<br>strategien</h3>
      <p class="service-text">Erstellung von energieeffizienten Sanierungsstrategien für Bauherren, die Sanierungsmaßnahmen planen um die energetischen Bilanz ihrer Gebäude zu verbessern mit dem Ziel hier die optimale Lösung erreichen.</p>
    </article>
    <article class="service" style="left:418px;top:36px">
      <svg class="service-icon" viewBox="0 0 32 34" fill="none" stroke="#fff" stroke-width="1.6" stroke-linejoin="round">
        <path d="M2 32h28M4 32V16h6v16M10 32V9l7-4v27M17 32V14h6v18M23 32V20h5v12M13 12h2M13 16h2M13 20h2M13 24h2M19 18h2M19 22h2M19 26h2"/>
      </svg>
      <h3 class="service-title">Spezialberechnungen</h3>
      <p class="service-text">Bauphysikalische Spezialberechnungen wie z.B. Wärmebrücken-Berechnungen zur Optimierung der EnEV Nachweise oder zur Feststellung von Feuchteproblematiken u. der Durchführung einer Schimmelanalyse.</p>
    </article>
    <article class="service" style="left:558px;top:36px">
      <svg class="service-icon" viewBox="0 0 32 34" fill="none" stroke="#fff" stroke-width="1.6" stroke-linecap="round" stroke-linejoin="round">
        <path d="M20 4c-4 3-6 6-6 9a6 6 0 0 0 12 0c0-3-2-6-6-9zM20 9v10"/><path d="M2 24l6-3 8 3h6a2 2 0 0 1 0 4H13M8 30l6 1 14-6"/>
      </svg>
      <h3 class="service-title">Beratung zu<br>Förderprogrammen</h3>
      <p class="service-text">Beratung zu den angebotenen Förderprogrammen zur Energieeinsparung und der Beantragung von öffentlichen Fördermitteln von der ZPT, der DUNO und weitere - wie z.B. regionale Förderer oder Kommunen.</p>
    </article>

    <div class="service-rule" style="left:139px;top:236px"></div>
    <div class="service-rule" style="left:277px;top:236px"></div>
    <div class="service-rule" style="left:418px;top:236px"></div>
    <div class="service-rule" style="left:560px;top:236px"></div>

    <article class="service" style="left:137px;top:254px">
      <svg class="service-icon" viewBox="0 0 32 34" fill="none" stroke="#fff" stroke-width="1.6" stroke-linecap="round" stroke-linejoin="round">
        <path d="M4 14L16 4l12 10v15a2 2 0 0 1-2 2H6a2 2 0 0 1-2-2z"/><path d="M16 31V16M16 24l-5-5M16 21l4-4"/>
      </svg>
      <h3 class="service-title">Baubegleitung</h3>
      <p class="service-text">Baubegleitung zur Sicherstellung der korrekten Durchführung der festgelegten und berechneten energetischen Werte auf der Baustelle selbst mit abschliessender Qualitätskontrolle und Dokumentation.</p>
    </article>
    <article class="service" style="left:277px;top:254px">
      <svg class="service-icon" viewBox="0 0 32 34" fill="none" stroke="#fff" stroke-width="1.6" stroke-linejoin="round">
        <path d="M18 2c1 6 10 9 10 19a12 12 0 0 1-24 0C4 13 12 9 18 2z"/><path d="M18 12l-6 10h6l-3 7 7-11h-6z"/>
      </svg>
      <h3 class="service-title">Energieausweisen</h3>
      <p class="service-text">Ausstellen von Energieausweisen u. die Erstellung von Energiebilanzen für Gewerbe- u. Industriegebäuden (nicht Wohngebäuden) und auch Wohnungen laut den Richtlinien der Energieeinsparverordnung - kurz EnEV und anderen europäischen Richtlinien.</p>
    </article>
    <article class="service" style="left:418px;top:254px">
      <svg class="service-icon" viewBox="0 0 32 34" fill="none" stroke="#fff" stroke-width="1.6" stroke-linejoin="round">
        <path d="M10 4a4 4 0 0 1 8 0v17a7 7 0 1 1-8 0z"/><circle cx="14" cy="26" r="3"/><path d="M14 23V10"/><path d="M27 8l-5 3 5 3z" fill="#fff"/>
      </svg>
      <h3 class="service-title">Messungen</h3>
      <p class="service-text">Durchführung von bauphysikalischen Messungen wie z.B die Differenzdruckmesssungen- auch Blower-Door Messungen genannt oder die Erstellung von thermografischen Aufnahmen um Schwachstellen z.B. an der Gebäudehülle sichtbar zu machen.</p>
    </article>
    <article class="service" style="left:558px;top:254px">
      <svg class="service-icon" viewBox="0 0 32 34" fill="none" stroke="#fff" stroke-width="1.6" stroke-linecap="round" stroke-linejoin="round">
        <path d="M16 2c-4 3-5 6-5 8a5 5 0 0 0 10 0c0-2-1-5-5-8zM16 7v12M6 19h20v4H6zM8 23l2 9h12l2-9"/>
      </svg>
      <h3 class="service-title">Betreuung auf<br>der Baustelle</h3>
      <p class="service-text">Vor - Ort - Betreuung auf der Baustelle in enger Zusammenarbeit mit dem Bauherren, dem Architekten, dem ausführendem Bauunternehmen und weiteren Dienstleistern.</p>
    </article>

    <div class="service-rule" style="left:139px;top:460px"></div>
    <div class="service-rule" style="left:277px;top:460px"></div>
    <div class="service-rule" style="left:418px;top:460px"></div>
    <div class="service-rule" style="left:560px;top:460px"></div>
  </section>

  <footer class="band contact">
    <div class="band-media" role="img" aria-label="Foto: Innenhof der Wohnanlage bei Nacht, stark abgedunkelt"></div>
    <h2 class="contact-title">Kontakt</h2>
    <div class="contact-rule"></div>
    <address class="contact-details">Vorname Nachname<br>Adresse<br>Telefon<br>E-Mail</address>
  </footer>

</div>
</body>
</html>
```